Business Card Design

We need a business card design for a Executive search firm based in London & the North East called Kelmscott. We specialise in mid - snr level (£50k - £200k) IT placements. Our company colour is navy blue.

Target Market(s)

CEO, HR Director, Sales Director/VP - (35 - 50), well educated, British, European & American

Industry/Entity Type

Business

Contact Information for Business Card

Kelmscott Talent Limited, Simon Trewella
Mobile - 0044 7700 318 642
London Office - Kelmscott House, 17 Birchcombe, Pinner. HA5 3QX
Tel: 00 44 20 718 46203
North East Office – Veltris Centre, Marlowe Lane, Hebburn, NE31 4GT
Tel: 00 44 191 4826053
www.kelmscotttalent-example.com

Also the same details for my Business Partner Ravi Sotkar
with his mobile number as 0044 7700 582731

Requirements
Must have
• must have the same logo

the logo needs to be the same but made sharper

```html
<!DOCTYPE html>
<html lang="en">
<head>
<meta charset="utf-8">
<title>Kelmscott Talent Limited – Business Cards</title>
<link rel="stylesheet" href="https://fonts.googleapis.com/css2?family=Lato:wght@400;700&display=swap">
<style>
  :root {
    --navy: #1c3a68;
    --navy-soft: #3b5a86;
    --white: #ffffff;
    --ink-grey: #6a6f78;
    --backdrop: #e6e8ec;
    --shadow: rgba(20, 30, 50, 0.18);
  }
  * { box-sizing: border-box; margin: 0; padding: 0; }
  html, body { width: 1200px; height: 926px; overflow: hidden; }
  body {
    background: var(--backdrop);
    font-family: "Lato", sans-serif;
    display: flex;
    flex-direction: column;
    align-items: center;
    justify-content: center;
    gap: 56px;
  }
  .card {
    position: relative;
    width: 620px;
    height: 376px;
    background: var(--white);
    box-shadow: 0 10px 28px var(--shadow);
    overflow: hidden;
  }
  .card__band {
    position: absolute;
    left: 0; right: 0; bottom: 0;
    background: var(--navy);
    color: var(--white);
  }
  .brand {
    display: flex;
    align-items: center;
    gap: 8px;
    color: var(--navy-soft);
    font-weight: 400;
    letter-spacing: 0.5px;
  }
  .brand__dot {
    width: 14px; height: 14px;
    border-radius: 50%;
    background: var(--navy-soft);
  }

  /* Company side */
  .card--company .card__band { top: 150px; text-align: center; }
  .card--company .brand {
    position: absolute;
    top: 58px; left: 50%;
    transform: translateX(-50%);
    font-size: 30px;
  }
  .company-title {
    margin-top: 70px;
    font-size: 36px;
    font-weight: 400;
    letter-spacing: 0.5px;
  }
  .company-web {
    margin-top: 14px;
    font-size: 17px;
    letter-spacing: 1.5px;
  }

  /* Personal side */
  .card--personal .card__band { top: 168px; }
  .card--personal .brand {
    position: absolute;
    top: 34px; left: 30px;
    font-size: 22px;
  }
  .contact {
    position: absolute;
    top: 28px; right: 28px;
    text-align: right;
    color: var(--navy);
  }
  .contact__name {
    font-size: 28px;
    font-weight: 400;
    letter-spacing: 1px;
    text-transform: uppercase;
    margin-bottom: 8px;
  }
  .contact__name strong { font-weight: 700; }
  .contact__line {
    display: flex;
    justify-content: flex-end;
    align-items: center;
    gap: 10px;
    font-size: 17px;
    line-height: 26px;
    color: var(--ink-grey);
    letter-spacing: 0.6px;
  }
  .contact__line--phone { color: var(--navy); font-size: 18px; }
  .contact__icon { width: 20px; height: 20px; flex: none; }
  .legal-name {
    position: absolute;
    top: 18px; left: 0; right: 0;
    text-align: center;
    font-size: 24px;
    font-weight: 400;
    letter-spacing: 1px;
    text-transform: uppercase;
  }
  .office {
    position: absolute;
    font-size: 13px;
    line-height: 18px;
    letter-spacing: 0.3px;
  }
  .office__title {
    font-size: 17px;
    letter-spacing: 0.8px;
    text-transform: uppercase;
    margin-bottom: 6px;
  }
  .office__tel b { font-weight: 700; }
  .office--london { top: 68px; left: 30px; }
  .office--north { bottom: 22px; right: 28px; text-align: right; }
</style>
</head>
<body>

  <section class="card card--company" aria-label="Company side of card">
    <div class="brand"><span class="brand__name">kelmscott</span><span class="brand__dot"></span></div>
    <div class="card__band">
      <h1 class="company-title">Kelmscott Talent Limited</h1>
      <p class="company-web">www.kelmscotttalent-example.com</p>
    </div>
  </section>

  <section class="card card--personal" aria-label="Personal side of card">
    <div class="brand"><span class="brand__name">kelmscott</span><span class="brand__dot"></span></div>

    <div class="contact">
      <h2 class="contact__name">Simon <strong>Trewella</strong></h2>
      <p class="contact__line contact__line--phone">0044 7700 318 642
        <svg class="contact__icon" viewBox="0 0 20 20" aria-hidden="true">
          <circle cx="10" cy="10" r="10" fill="var(--navy)"/>
          <rect x="6.5" y="4" width="7" height="12" rx="1.3" fill="none" stroke="#fff" stroke-width="1.4"/>
          <circle cx="10" cy="13.6" r="0.9" fill="#fff"/>
        </svg>
      </p>
      <p class="contact__line">www.kelmscotttalent-example.com
        <svg class="contact__icon" viewBox="0 0 20 20" aria-hidden="true">
          <circle cx="10" cy="10" r="10" fill="var(--navy)"/>
          <rect x="5" y="8.5" width="6" height="3.4" rx="1.7" transform="rotate(-45 8 10.2)" fill="none" stroke="#fff" stroke-width="1.3"/>
          <rect x="9" y="8.2" width="6" height="3.4" rx="1.7" transform="rotate(-45 12 9.9)" fill="none" stroke="#fff" stroke-width="1.3"/>
        </svg>
      </p>
    </div>

    <div class="card__band">
      <p class="legal-name">Kelmscott Talent Limited</p>
      <div class="office office--london">
        <p class="office__title">London Office</p>
        <p class="office__tel"><b>Tel:</b> 00 44 20 718 46203</p>
        <p>Kelmscott House, 17 Birchcombe,</p>
        <p>Pinner. HA5 3QX</p>
      </div>
      <div class="office office--north">
        <p class="office__title">North East Office</p>
        <p class="office__tel">Tel: 00 44 191 4826053</p>
        <p>Veltris Centre, Marlowe Lane,</p>
        <p>Hebburn, NE31 4GT</p>
      </div>
    </div>
  </section>

</body>
</html>
```